Sturdyflow Mechanical - Letterhead

We are a plumbing and hvac company based in Calgary. This letterhead will be on our quotes, invoices, preventative maintenance proposals etc.

```html
<!DOCTYPE html>
<html lang="en">
<head>
<meta charset="utf-8">
<title>Sturdyflow Mechanical – Letterhead</title>
<link href="https://fonts.googleapis.com/css2?family=Carlito:wght@400;700&family=Open+Sans:wght@400&display=swap" rel="stylesheet">
<style>
  :root {
    --orange: #ee6a3a;
    --blue: #3a78bf;
    --grey: #77787b;
    --ink: #3b3b3b;
    --paper: #ffffff;
    --signature-tone: #dbe6f3;
  }
  * { box-sizing: border-box; margin: 0; padding: 0; }
  html, body { width: 1056px; height: 1200px; overflow: hidden; background: var(--paper); }
  .letterhead {
    position: relative; width: 1056px; height: 1200px;
    background: var(--paper); color: var(--ink);
    font-family: "Carlito", "Calibri", sans-serif;
  }
  .brand {
    position: absolute; left: 108px; top: 72px;
    display: flex; align-items: center; gap: 16px;
  }
  .brand-dot { width: 54px; height: 54px; border-radius: 50%; background: var(--orange); flex: none; }
  .brand-name {
    font-family: "Carlito", "Calibri", sans-serif; font-weight: 700;
    font-size: 38px; line-height: 40px; color: var(--blue);
  }
  .contact {
    position: absolute; left: 681px; top: 74px; height: 113px;
    border-left: 2px solid var(--orange); padding-left: 24px;
    font-family: "Open Sans", sans-serif; font-size: 15px; font-style: normal; color: var(--ink);
  }
  .contact-item { display: flex; align-items: flex-start; gap: 10px; line-height: 23px; }
  .contact-item svg { flex: none; margin-top: 4px; }
  .contact-line { display: block; }
  .letter-date { position: absolute; left: 108px; top: 296px; font-size: 15px; }
  .recipient { position: absolute; left: 108px; top: 342px; font-size: 15px; line-height: 23.5px; }
  .salutation { position: absolute; left: 108px; top: 464px; font-size: 22px; font-weight: 700; }
  .letter-body { position: absolute; left: 108px; top: 516px; width: 840px; font-size: 15px; line-height: 23.5px; text-align: justify; }
  .letter-body p + p { margin-top: 23px; }
  .closing { position: absolute; left: 108px; top: 940px; font-size: 15px; }
  .signature { position: absolute; left: 108px; top: 990px; width: 130px; height: 40px; background: var(--signature-tone); border-radius: 4px; }
  .footer-bands { position: absolute; left: 0; bottom: 0; width: 1056px; height: 16px; display: flex; gap: 4px; }
  .band { flex: 1; }
  .band--orange { background: var(--orange); }
  .band--blue { background: var(--blue); }
  .band--grey { background: var(--grey); }
</style>
</head>
<body>
<main class="letterhead">
  <header>
    <div class="brand">
      <span class="brand-dot"></span>
      <span class="brand-name">Sturdyflow<br>Mechanical</span>
    </div>
    <address class="contact">
      <div class="contact-item">
        <svg width="14" height="14" viewBox="0 0 14 14"><circle cx="7" cy="7" r="7" fill="var(--orange)"/><path d="M7 3.2a2.4 2.4 0 0 0-2.4 2.4C4.6 7.5 7 10.6 7 10.6s2.4-3.1 2.4-5A2.4 2.4 0 0 0 7 3.2z" fill="#fff"/><circle cx="7" cy="5.6" r="0.9" fill="var(--orange)"/></svg>
        <span><span class="contact-line">410 Harlow Street #800</span><span class="contact-line">Calgary, AB T2P 1J9</span></span>
      </div>
      <div class="contact-item">
        <svg width="14" height="14" viewBox="0 0 14 14"><circle cx="7" cy="7" r="7" fill="var(--orange)"/><path d="M4 5.2c0-.8 6-.8 6 0v.8H8.6v-.6H5.4v.6H4zM4.6 6.6h4.8l.6 3H4z" fill="#fff"/></svg>
        <span>877-555-FLOW</span>
      </div>
      <div class="contact-item">
        <svg width="14" height="14" viewBox="0 0 14 14"><circle cx="7" cy="7" r="7" fill="var(--orange)"/><circle cx="7" cy="7" r="3.6" fill="none" stroke="#fff" stroke-width="1.2"/><circle cx="7" cy="7" r="1.3" fill="#fff"/></svg>
        <span>info@sturdyflowmech.com</span>
      </div>
      <div class="contact-item">
        <svg width="14" height="14" viewBox="0 0 14 14"><circle cx="7" cy="7" r="7" fill="var(--orange)"/><rect x="3.6" y="4.6" width="6.8" height="4.8" rx="0.6" fill="#fff"/><path d="M3.8 4.9 7 7.4l3.2-2.5" fill="none" stroke="var(--orange)" stroke-width="0.8"/></svg>
        <span>www.sturdyflowmech.com</span>
      </div>
    </address>
  </header>

  <p class="letter-date">September 10th, 2020</p>
  <p class="recipient">First Last Name<br>Street Address<br>City, State 00000</p>
  <p class="salutation">Dear Sir / Mam,</p>

  <section class="letter-body">
    <p>Lorem ipsum dolor sit amet, consectetur adipiscing elit. Aenean ut ipsum eget massa hendrerit vestibulum vel in velit. Donec pretium neque velit.</p>
    <p>Aliquam porta lectus nec mauris ornare venenatis. Vivamus non est turpis, et cursus sem. Mauris vehicula erat in diam auctor at bibendum nisl lacinia.</p>
    <p>Morbi imperdiet neque vehicula nunc convallis gravida. Vestibulum iaculis pretium placerat. Integer consequat, est sit amet facilisis eleifend, nibh nibh varius orci, eget dapibus arcu dui non purus. Pellentesque in magna mauris. Duis enim sapien, dictum vitae condimentum a, pulvinar vel lacus. Mauris et molestie nibh. Vestibulum vitae nulla at metus elementum porta sit amet interdum elit. Nulla sollicitudin neque eu nulla volutpat congue.</p>
    <p>Etiam pellentesque, velit id dapibus fermentum, turpis sapien ornare dui, ac tincidunt ligula odio congue purus. Nunc sed ante dui, in porta lectus. Cras nec sem lorem. In hac habitasse platea dictumst. Maecenas id diam quis dui porta tristique. Sed id egestas felis. Donec ullamcorper mattis posuere. Phasellus fermentum eleifend tortor vel dapibus. Vestibulum ante ipsum.</p>
  </section>

  <p class="closing">Your Sincerely,</p>
  <div class="signature" role="img" aria-label="Handwritten signature of the sender"></div>

  <footer class="footer-bands">
    <span class="band band--orange"></span>
    <span class="band band--blue"></span>
    <span class="band band--grey"></span>
  </footer>
</main>
</body>
</html>
```